Lydfern Primary School

We need to improve on our designs for a local School, Lydfern Primary.
One file contains the correct information required on the sign.
Our Mock ups are suggestions.
The School Uniform is blue -
We had these comments from our Client.
I can't decide whether to change the blue and try green to represent our commitment to outdoors, or maybe a combination of colours from the school badge, For the main sign options , I like them both but wondered if there was a way of combining the two? Slightly bigger badge.

I've included the files for the smaller signs if you were happy to provide a service to include all. We are a sign business focusing on other projects and external support will help. Thanks - Dermot.

```html
<!DOCTYPE html>
<html lang="en">
<head>
<meta charset="utf-8">
<title>Lydfern Primary School – Sign Options</title>
<link href="https://fonts.googleapis.com/css2?family=Outfit:wght@500;600;700&display=swap" rel="stylesheet">
<style>
  :root {
    --page: #eefad0;
    --sign-blue: #1178c0;
    --band-green: #9ccb3b;
    --word-green: #9fd03a;
    --sun-yellow: #f7d54a;
    --sun-orange: #f28f22;
    --navy: #133e6e;
    --white: #ffffff;
    --hill-green: #3f9a6e;
    --sky-light: #4d9ad4;
  }
  html, body {
    margin: 0;
    padding: 0;
    width: 786px;
    height: 1200px;
    overflow: hidden;
    background: var(--page);
  }
  .sign-sheet {
    display: block;
    width: 786px;
    height: 1200px;
    font-family: "Outfit", sans-serif;
  }
  .sign-body { fill: var(--sign-blue); }
  .phone-band { fill: var(--band-green); }
  .welcome-word { fill: var(--word-green); font-weight: 700; }
  .motto { fill: var(--sun-yellow); font-weight: 500; }
  .school-name { fill: var(--white); font-weight: 700; }
  .phone-number { fill: var(--navy); font-weight: 700; }
  .phone-icon { fill: var(--navy); }
  .badge-disc { fill: var(--sun-orange); }
  .badge-initials { fill: var(--white); font-weight: 700; }
  .accent-blocks { fill: var(--sun-yellow); opacity: 0.9; }
  .divider { stroke: var(--sun-yellow); stroke-width: 1; }
  .shadow { filter: drop-shadow(0 8px 14px rgba(80, 110, 20, 0.22)); }
</style>
</head>
<body>
<svg class="sign-sheet" viewBox="0 0 786 1200" xmlns="http://www.w3.org/2000/svg">
  <defs>
    <linearGradient id="landscapeFade" x1="0" y1="0" x2="0" y2="1">
      <stop offset="0" stop-color="#1178c0" stop-opacity="0"/>
      <stop offset="0.5" stop-color="#4d9ad4" stop-opacity="0.55"/>
      <stop offset="1" stop-color="#3f9a6e" stop-opacity="0.9"/>
    </linearGradient>
    <linearGradient id="blockFade" x1="0" y1="0" x2="1" y2="1">
      <stop offset="0" stop-color="#9ccb3b"/>
      <stop offset="0.5" stop-color="#f7d54a"/>
      <stop offset="1" stop-color="#f28f22"/>
    </linearGradient>
    <clipPath id="clipWide"><rect x="84" y="80" width="619" height="296" rx="20"/></clipPath>
    <clipPath id="clipArched">
      <path d="M92,546 C200,546 280,540 318,515 A76,76 0 1 1 470,515 C508,540 588,546 694,546 Q704,546 704,556 V826 Q704,836 694,836 H92 Q82,836 82,826 V556 Q82,546 92,546 Z"/>
    </clipPath>
    <clipPath id="clipRounded">
      <path d="M194,908 H693 Q703,908 703,918 V1111 Q703,1121 693,1121 H194 A106.5,106.5 0 0 1 194,908 Z"/>
    </clipPath>
    <symbol id="handset" viewBox="0 0 24 24">
      <path d="M6.6 10.8c1.4 2.8 3.8 5.1 6.6 6.6l2.2-2.2c.3-.3.7-.4 1-.2 1.1.4 2.3.6 3.6.6.6 0 1 .4 1 1V20c0 .6-.4 1-1 1C10.6 21 3 13.4 3 4c0-.6.4-1 1-1h3.5c.6 0 1 .4 1 1 0 1.3.2 2.5.6 3.6.1.3 0 .7-.2 1L6.6 10.8z"/>
    </symbol>
  </defs>

  <!-- Option one: wide rectangular sign -->
  <g class="sign sign-wide">
    <rect class="sign-body shadow" x="84" y="80" width="619" height="296" rx="20"/>
    <g clip-path="url(#clipWide)">
      <rect role="img" aria-label="Illustrated countryside: hills, trees, a small house and sun rays" x="84" y="210" width="290" height="114" fill="url(#landscapeFade)"/>
      <rect role="img" aria-label="Colourful geometric corner blocks" class="accent-blocks" x="84" y="80" width="44" height="88" fill="url(#blockFade)"/>
      <rect role="img" aria-label="Colourful geometric corner blocks" class="accent-blocks" x="636" y="234" width="67" height="89" fill="url(#blockFade)"/>
      <rect class="phone-band" x="84" y="323" width="619" height="53"/>
    </g>
    <circle class="badge-disc" cx="394" cy="150" r="50"/>
    <text class="badge-initials" x="394" y="160" font-size="28" text-anchor="middle">LPS</text>
    <text class="welcome-word" x="245" y="196" font-size="29" text-anchor="middle" textLength="136" lengthAdjust="spacingAndGlyphs">WELCOME</text>
    <text class="welcome-word" x="529" y="196" font-size="29" text-anchor="middle" textLength="112" lengthAdjust="spacingAndGlyphs">CROESO</text>
    <text class="motto" x="394" y="240" font-size="19" text-anchor="middle" textLength="332" lengthAdjust="spacingAndGlyphs">'WINGS TO FLY, ROOTS TO GROW'</text>
    <text class="school-name" x="394" y="292" font-size="44" text-anchor="middle" textLength="454" lengthAdjust="spacingAndGlyphs">Lydfern Primary School</text>
    <use class="phone-icon" href="#handset" x="280" y="335" width="26" height="26"/>
    <text class="phone-number" x="412" y="361" font-size="30" text-anchor="middle" textLength="190" lengthAdjust="spacingAndGlyphs">01632 960481</text>
  </g>

  <!-- Option two: arched sign with raised badge -->
  <g class="sign sign-arched">
    <path class="sign-body shadow" d="M92,546 C200,546 280,540 318,515 A76,76 0 1 1 470,515 C508,540 588,546 694,546 Q704,546 704,556 V826 Q704,836 694,836 H92 Q82,836 82,826 V556 Q82,546 92,546 Z"/>
    <g clip-path="url(#clipArched)">
      <rect role="img" aria-label="Illustrated countryside: hills, trees, mountains, a small house and sun rays" x="330" y="640" width="374" height="140" fill="url(#landscapeFade)"/>
      <rect role="img" aria-label="Colourful geometric corner blocks" class="accent-blocks" x="636" y="546" width="68" height="90" fill="url(#blockFade)"/>
      <rect role="img" aria-label="Colourful geometric corner blocks" class="accent-blocks" x="82" y="746" width="45" height="90" fill="url(#blockFade)"/>
      <rect class="phone-band" x="82" y="780" width="622" height="56"/>
    </g>
    <circle class="badge-disc" cx="394" cy="519" r="64"/>
    <text class="badge-initials" x="394" y="530" font-size="32" text-anchor="middle">LPS</text>
    <text class="welcome-word" x="388" y="639" font-size="32" text-anchor="middle" textLength="286" lengthAdjust="spacingAndGlyphs">WELCOME CROESO</text>
    <text class="motto" x="386" y="688" font-size="21" text-anchor="middle" textLength="371" lengthAdjust="spacingAndGlyphs">'WINGS TO FLY, ROOTS TO GROW'</text>
    <text class="school-name" x="386" y="748" font-size="48" text-anchor="middle" textLength="510" lengthAdjust="spacingAndGlyphs">Lydfern Primary School</text>
    <use class="phone-icon" href="#handset" x="277" y="791" width="28" height="28"/>
    <text class="phone-number" x="410" y="819" font-size="32" text-anchor="middle" textLength="196" lengthAdjust="spacingAndGlyphs">01632 960481</text>
  </g>

  <!-- Option three: rounded-end sign with side badge -->
  <g class="sign sign-rounded">
    <path class="sign-body shadow" d="M194,908 H693 Q703,908 703,918 V1111 Q703,1121 693,1121 H194 A106.5,106.5 0 0 1 194,908 Z"/>
    <g clip-path="url(#clipRounded)">
      <rect role="img" aria-label="Illustrated countryside: hills, trees and a small house" x="440" y="1000" width="263" height="67" fill="url(#landscapeFade)"/>
      <rect role="img" aria-label="Colourful geometric corner blocks" class="accent-blocks" x="636" y="908" width="67" height="90" fill="url(#blockFade)"/>
      <rect class="phone-band" x="194" y="1067" width="509" height="54"/>
      <circle class="sign-body" cx="194" cy="1015" r="107"/>
    </g>
    <circle class="badge-disc" cx="194" cy="1015" r="84"/>
    <text class="badge-initials" x="194" y="1029" font-size="40" text-anchor="middle">LPS</text>
    <text class="welcome-word" x="302" y="959" font-size="20" textLength="180" lengthAdjust="spacingAndGlyphs">WELCOME CROESO</text>
    <line class="divider" x1="302" y1="971" x2="506" y2="971"/>
    <text class="motto" x="302" y="1001" font-size="16" textLength="272" lengthAdjust="spacingAndGlyphs">'WINGS TO FLY, ROOTS TO GROW'</text>
    <text class="school-name" x="302" y="1044" font-size="35" textLength="374" lengthAdjust="spacingAndGlyphs">Lydfern Primary School</text>
    <use class="phone-icon" href="#handset" x="302" y="1082" width="22" height="22"/>
    <text class="phone-number" x="330" y="1102" font-size="26" textLength="170" lengthAdjust="spacingAndGlyphs">01632 960481</text>
  </g>
</svg>
</body>
</html>
```